Architecture firm needing a business card

We need a business card design for a new company based in the US called "Pellmore Architecture". Seeking minimalist designs that have a creativity/design feel but must be clean and professional. Please refer to the logo attached.

Target Market(s)

Real Estate Investors, Home Builders and Construction Firms.

Industry/Entity Type

Architecture

Contact Information for Business Card

Standard US size business cards. Would like to have some sort of graphic on the back side of the card - nothing that is too loud but something that may catch your attention. More or less grayscale colors that are in line with the logo colors (navy and greys essentially). Additional colors maybe accepted if blended properly (earthtones), but might be difficult to accomplish and maintain the clean/minimalist look.

Requirements
Must have
• Clean Lines
Nice to have
• some sort of graphics, would like to have something creative on the back side of the card
Should not have
• nothing too busy, cluttered or overwhelming.

```html
<!DOCTYPE html>
<html lang="en">
<head>
<meta charset="utf-8">
<title>Pellmore Architecture — Business Card</title>
<link rel="stylesheet" href="https://fonts.googleapis.com/css2?family=Arimo:wght@400;700&display=swap">
<style>
  :root {
    --backdrop: #2a2a2a;
    --card: #ffffff;
    --navy: #1f3a5f;
    --ink: #3c3c3c;
    --shadow: rgba(0, 0, 0, 0.45);
  }
  * { margin: 0; padding: 0; box-sizing: border-box; }
  html, body {
    width: 1200px;
    height: 900px;
    overflow: hidden;
    background: var(--backdrop);
    font-family: "Arimo", Arial, sans-serif;
  }
  .canvas {
    width: 1200px;
    height: 900px;
    display: flex;
    flex-direction: column;
    align-items: center;
    justify-content: center;
    gap: 44px;
  }
  .card {
    position: relative;
    width: 660px;
    height: 377px;
    background: var(--card);
    box-shadow: 0 10px 28px var(--shadow);
  }
  .wordmark {
    display: flex;
    align-items: center;
    gap: 12px;
    color: var(--navy);
    font-weight: 400;
    text-transform: uppercase;
    white-space: nowrap;
  }
  .wordmark-square {
    width: 34px;
    height: 34px;
    background: var(--navy);
    flex: none;
  }
  .wordmark-text { display: flex; flex-direction: column; line-height: 1; }
  .wordmark-main { font-size: 30px; letter-spacing: 0.02em; }
  .wordmark-sub { font-size: 13px; letter-spacing: 0.2em; margin-top: 3px; }
  .card-front .wordmark {
    position: absolute;
    top: 50%;
    left: 50%;
    transform: translate(-50%, -50%);
  }
  .card-back .wordmark {
    position: absolute;
    top: 32px;
    left: 32px;
  }
  .person {
    position: absolute;
    top: 150px;
    left: 385px;
    color: var(--ink);
    line-height: 1.1;
  }
  .person-name { font-size: 19px; font-weight: 700; }
  .person-title { font-size: 15px; padding-left: 30px; }
  .contact {
    position: absolute;
    top: 232px;
    left: 405px;
    list-style: none;
    color: var(--ink);
    font-size: 15px;
    line-height: 1.3;
  }
</style>
</head>
<body>
  <main class="canvas">
    <section class="card card-front" aria-label="Card front">
      <div class="wordmark">
        <span class="wordmark-square"></span>
        <span class="wordmark-text"><span class="wordmark-main">Pellmore</span><span class="wordmark-sub">Architecture</span></span>
      </div>
    </section>
    <section class="card card-back" aria-label="Card back">
      <div class="wordmark">
        <span class="wordmark-square"></span>
        <span class="wordmark-text"><span class="wordmark-main">Pellmore</span><span class="wordmark-sub">Architecture</span></span>
      </div>
      <div class="person">
        <p class="person-name">Name</p>
        <p class="person-title">Title</p>
      </div>
      <ul class="contact">
        <li>Phone : 00 00 000 000</li>
        <li>Cell : 00000 00000</li>
        <li>email : name@company.com</li>
        <li>www.yourcompany.com</li>
        <li>Address 1, Address 2,</li>
        <li>Address 3, Address 4</li>
      </ul>
    </section>
  </main>
</body>
</html>
```